Darlene Whitcott

I need all of my logos on one card. I would like a burgundy back and Harbor Shield and Tamsworth insurance being the most prominent.
Phone Number 541-382-9154
Web:
www.Tamsworthins.example
www.Harbor Shield.example
www.Kell-Insurance.example

```html
<!DOCTYPE html>
<html lang="en">
<head>
<meta charset="utf-8">
<title>Darlene Whitcott – Business Card</title>
<link rel="stylesheet" href="https://fonts.googleapis.com/css2?family=Cinzel:wght@500;600&family=Crimson+Text&family=Montserrat:wght@500&display=swap">
<style>
  :root {
    --bg: #e6e3e2;
    --paper: #fbfbfa;
    --gold: #c9a20a;
    --burgundy: #4a1020;
    --ink: #1b1b1b;
  }
  * { box-sizing: border-box; margin: 0; padding: 0; }
  html, body { width: 1200px; height: 788px; overflow: hidden; background: var(--bg); }
  .stage { position: relative; width: 1200px; height: 788px; }

  .card {
    position: absolute;
    top: 106px;
    width: 318px;
    height: 534px;
    background: var(--paper);
    overflow: hidden;
  }
  .card--front { left: 242px; }
  .card--back { left: 653px; }

  /* Front: brand names */
  .brand-stack {
    display: flex;
    flex-direction: column;
    align-items: center;
    justify-content: space-around;
    height: 100%;
    padding: 60px 20px 40px;
  }
  .brand {
    font-family: "Cinzel", serif;
    font-weight: 600;
    color: var(--gold);
    text-align: center;
    line-height: 1.05;
    letter-spacing: 1px;
  }
  .brand--lead { font-size: 30px; }
  .brand--second { font-size: 30px; }
  .brand--agency { font-size: 22px; }
  .brand--farm { font-size: 20px; }

  /* Back */
  .back-art { position: absolute; inset: 0; }
  .call {
    position: absolute;
    top: 78px;
    width: 100%;
    text-align: center;
    font-family: "Cinzel", serif;
    font-weight: 500;
    font-size: 28px;
    color: var(--gold);
    white-space: nowrap;
  }
  .enquiry {
    position: absolute;
    top: 118px;
    width: 100%;
    display: flex;
    align-items: center;
    justify-content: center;
    gap: 8px;
    font-family: "Montserrat", sans-serif;
    font-weight: 500;
    font-size: 11.5px;
    letter-spacing: 0.5px;
    color: var(--ink);
  }
  .enquiry::before, .enquiry::after {
    content: "";
    width: 22px;
    height: 2px;
    background: var(--ink);
  }
  .services {
    position: absolute;
    top: 242px;
    width: 100%;
    list-style: none;
    text-align: center;
    font-family: "Cinzel", serif;
    font-weight: 500;
    font-size: 15.5px;
    color: var(--ink);
  }
  .services li { height: 28.6px; }
  .sites {
    position: absolute;
    top: 434px;
    left: 68px;
    right: 68px;
    list-style: none;
    text-align: center;
    font-family: "Crimson Text", serif;
    font-size: 13.5px;
    color: var(--ink);
  }
  .sites li { height: 23.5px; line-height: 23px; }
  .sites li + li { border-top: 1px solid rgba(27,27,27,0.45); }
</style>
</head>
<body>
<main class="stage">

  <section class="card card--front" aria-label="Card front">
    <div class="brand-stack">
      <p class="brand brand--lead">TAMSWORTH<br>INSURANCE</p>
      <p class="brand brand--second">HARBOR SHIELD<br>INC</p>
      <p class="brand brand--agency">WARREN KELL<br>AGENCY INC</p>
      <p class="brand brand--farm">TAMSWORTH INSURANCE<br>FARM &amp; RANCH</p>
    </div>
  </section>

  <section class="card card--back" aria-label="Card back">
    <svg class="back-art" width="318" height="534" viewBox="0 0 318 534" aria-hidden="true">
      <path d="M0 158 C 90 200, 220 215, 318 156 L318 534 L0 534 Z" fill="var(--burgundy)"/>
      <path d="M0 192 C 100 210, 230 205, 318 156 L318 534 L0 534 Z" fill="var(--gold)"/>
    </svg>
    <p class="call">CALL: 541-382-9154</p>
    <p class="enquiry">FOR INSURANCE ENQUIRY</p>
    <ul class="services">
      <li>BUSINESS INSURANCE</li>
      <li>AUTO INSURANCE</li>
      <li>HOME INSURANCE</li>
      <li>LIFE INSURANCE</li>
      <li>FARM &amp; RANCH INSURANCE</li>
      <li>HEALTH INSURANCE</li>
    </ul>
    <ul class="sites">
      <li>www.Tamsworthins.example</li>
      <li>www.Harbor Shield.example</li>
      <li>www.Kell-Insurance.example</li>
    </ul>
  </section>

</main>
</body>
</html>
```